Graphics Design of Physics Book

Hi
Size : 8" x 11.25"
We are education book Publication Company and would like to have book cover for "Physics" it has 4 volumes. All 4 having the same color scheme and design except the volume no.
Blue is my personal favorite but u can use any color. Want to have a band at the bottom of the cover to place our Logo “VORLIN Education” a PDF of the same is attached, or you can place logo anywhere according to ur design.
I need “Physics” as title of the book to be visible prominently.
And volume and volume no. should also be Visible and eye catching I prefer a Graphic to enhance the Volume No.
A background pattern can also be a option (it should be vector form so that color can be change later)
Please do not offer any cut and paste design I need very professional presentation.
Volume and Number can be in metallic 3D (CMYK) effect.
only Professional presentation will get feedback.
I have provided a sample artwork for reference do not follow it but can be a reference what I needed !

Target Market(s)

Students Class 9th to 12th

Industry/Entity Type

Education

Font styles to use
Serif

Colors
3176b5
0555a3
85abd2
cadf82
abd036
9bcb3c

Requirements
Must have
• Eye catching.
• “Physics” as title of the book to be visible prominently.
• volume and volume no. should also be Visible and eye catching
• I prefer a Graphic to enhance the Volume No.
• Icons for
• 1. Questions and answers
• 2. Theory Notes
• 3. Tips & Tricks
• 4. Previous Year's Reference Questions
• 5. Covers Complete Syllabus
Nice to have
• decent seamless background or metallic 3d effect (not to be print in special Ink) design should only be in CMYK.
Should not have
• Physics related Pictures or Icons (Specially E=mc2) or any scientist photograph or I Need pure graphic design

```html
<!DOCTYPE html>
<html lang="en">
<head>
<meta charset="utf-8">
<title>Physics Volume 2 – Cover</title>
<link href="https://fonts.googleapis.com/css2?family=Sora:wght@700;800&family=Roboto:wght@400;500;700&display=swap" rel="stylesheet">
<style>
  :root {
    --sky: #18a4ea;
    --ocean: #1565c8;
    --royal: #283d9e;
    --navy: #2a2d86;
    --ink: #1e2270;
    --gold-light: #ffe39a;
    --gold: #f2a530;
    --gold-deep: #b86a1e;
    --white: #ffffff;
    --black: #111111;
  }
  * { margin: 0; padding: 0; box-sizing: border-box; }
  html, body { width: 849px; height: 1200px; overflow: hidden; background: var(--white); }
  .cover {
    position: relative;
    width: 849px;
    height: 1200px;
    overflow: hidden;
    font-family: "Roboto", sans-serif;
    background: var(--white);
  }
  .cover__field {
    position: absolute;
    left: 0; top: 0;
    width: 849px; height: 1037px;
    background:
      radial-gradient(ellipse 520px 200px at 260px 330px, rgba(120,215,255,0.55), transparent 70%),
      radial-gradient(ellipse 600px 260px at 560px 160px, rgba(60,190,250,0.5), transparent 70%),
      linear-gradient(180deg, var(--sky) 0%, var(--ocean) 30%, var(--royal) 55%, var(--navy) 80%, var(--ink) 100%);
  }
  .cover__swirl {
    position: absolute;
    left: 0; top: 0;
    width: 849px; height: 640px;
    background:
      radial-gradient(ellipse 700px 120px at 300px 420px, rgba(170,230,255,0.35), transparent 70%),
      radial-gradient(ellipse 300px 90px at 60px 280px, rgba(230,248,255,0.55), transparent 70%);
  }
  .title, .volume-number {
    position: absolute;
    left: 0; top: 0;
  }
  .features {
    position: absolute;
    left: 0; top: 708px;
    width: 849px; height: 110px;
  }
  .feature {
    position: absolute;
    width: 180px;
    margin-left: -90px;
    text-align: center;
    color: var(--white);
  }
  .feature svg { display: block; margin: 0 auto; }
  .feature__label {
    margin-top: 8px;
    font-size: 14.5px;
    line-height: 18px;
    letter-spacing: -0.2px;
  }
  .dot-band {
    position: absolute;
    left: 0; top: 850px;
    width: 849px; height: 144px;
    background:
      linear-gradient(90deg, var(--ink) 0%, #2c3aa0 30%, #3ea6e6 55%, #2c3aa0 78%, var(--ink) 100%);
    border-top: 4px solid var(--sky);
    border-bottom: 4px solid var(--sky);
  }
  .gold-rule {
    position: absolute;
    left: 0; top: 1012px;
    width: 849px; height: 12px;
    background: linear-gradient(90deg, var(--gold-deep), var(--gold-light) 22%, var(--gold-deep) 40%, var(--gold-light) 55%, var(--gold-deep) 75%, var(--gold-light) 88%, var(--gold-deep));
  }
  .brand {
    position: absolute;
    left: 0; top: 1090px;
    width: 849px;
    text-align: center;
    font-family: "Roboto", sans-serif;
    font-weight: 700;
    font-size: 30px;
    letter-spacing: 2px;
    color: var(--black);
  }
</style>
</head>
<body>
<main class="cover">
  <div class="cover__field"></div>
  <div class="cover__swirl" role="img" aria-label="Abstract flowing blue light swirl background"></div>

  <svg class="title" width="849" height="240" viewBox="0 0 849 240" aria-label="Physics">
    <text x="72" y="211" textLength="708" lengthAdjust="spacingAndGlyphs"
          font-family="Sora, sans-serif" font-weight="800" font-size="168" fill="#ffffff">PHYSICS</text>
  </svg>

  <svg class="volume-number" width="849" height="700" viewBox="0 0 849 700" aria-label="Volume 2">
    <defs>
      <linearGradient id="goldFace" x1="0" y1="0" x2="0.4" y2="1">
        <stop offset="0" stop-color="#f0b347"/>
        <stop offset="0.3" stop-color="#ffe7a0"/>
        <stop offset="0.55" stop-color="#f2a530"/>
        <stop offset="0.8" stop-color="#ffd98a"/>
        <stop offset="1" stop-color="#f0ac3e"/>
      </linearGradient>
      <linearGradient id="goldEdge" x1="0" y1="0" x2="1" y2="1">
        <stop offset="0" stop-color="#fff0c0"/>
        <stop offset="0.5" stop-color="#b86a1e"/>
        <stop offset="1" stop-color="#ffe39a"/>
      </linearGradient>
    </defs>
    <text x="457" y="673" textLength="267" lengthAdjust="spacingAndGlyphs"
          font-family="Sora, sans-serif" font-weight="700" font-size="520"
          fill="url(#goldFace)" stroke="url(#goldEdge)" stroke-width="12" paint-order="stroke">2</text>
  </svg>

  <section class="features">
    <div class="feature" style="left:120px">
      <svg width="90" height="62" viewBox="0 0 90 62">
        <path d="M8 30 a24 24 0 1 1 14 22 l-16 6 z" fill="#ffffff" stroke="#2a2d86" stroke-width="2"/>
        <text x="32" y="40" text-anchor="middle" font-family="Roboto, sans-serif" font-weight="700" font-size="30" fill="#2a2d86">?</text>
        <path d="M48 46 a18 18 0 1 1 30 12 l10 4 l-18 -2 a18 18 0 0 1 -22 -14 z" fill="#2a2d86" stroke="#ffffff" stroke-width="3"/>
        <text x="64" y="55" text-anchor="middle" font-family="Roboto, sans-serif" font-weight="700" font-size="20" fill="#ffffff">A</text>
      </svg>
      <div class="feature__label">Questions<br>&amp; Answers</div>
    </div>
    <div class="feature" style="left:255px">
      <svg width="62" height="62" viewBox="0 0 62 62">
        <circle cx="31" cy="31" r="28" fill="#2a2d86" stroke="#ffffff" stroke-width="3"/>
        <path d="M31 16 a11 11 0 0 0 -6 20 v5 h12 v-5 a11 11 0 0 0 -6 -20 z" fill="none" stroke="#ffffff" stroke-width="2.5"/>
        <line x1="26" y1="45" x2="36" y2="45" stroke="#ffffff" stroke-width="2.5"/>
        <g stroke="#ffffff" stroke-width="2">
          <line x1="31" y1="8" x2="31" y2="12"/><line x1="17" y1="14" x2="20" y2="17"/><line x1="45" y1="14" x2="42" y2="17"/>
          <line x1="12" y1="27" x2="16" y2="27"/><line x1="50" y1="27" x2="46" y2="27"/>
        </g>
      </svg>
      <div class="feature__label">Tips &amp; Tricks</div>
    </div>
    <div class="feature" style="left:395px">
      <svg width="62" height="62" viewBox="0 0 62 62">
        <rect x="3" y="3" width="56" height="56" rx="8" fill="#1e7fd0" stroke="#ffffff" stroke-width="3"/>
        <rect x="17" y="13" width="26" height="36" rx="2" fill="none" stroke="#ffffff" stroke-width="2.5"/>
        <g stroke="#ffffff" stroke-width="2"><line x1="22" y1="21" x2="34" y2="21"/><line x1="22" y1="28" x2="32" y2="28"/><line x1="22" y1="35" x2="28" y2="35"/></g>
        <path d="M44 22 l5 5 l-14 14 l-6 1 l1 -6 z" fill="#1e7fd0" stroke="#ffffff" stroke-width="2.2"/>
      </svg>
      <div class="feature__label">Theory Notes</div>
    </div>
    <div class="feature" style="left:558px">
      <svg width="62" height="62" viewBox="0 0 62 62">
        <rect x="3" y="3" width="56" height="56" rx="8" fill="#2a2d86" stroke="#ffffff" stroke-width="3"/>
        <rect x="15" y="12" width="26" height="34" fill="none" stroke="#ffffff" stroke-width="2.5"/>
        <g stroke="#ffffff" stroke-width="2"><line x1="20" y1="20" x2="36" y2="20"/><line x1="20" y1="26" x2="36" y2="26"/><line x1="20" y1="32" x2="30" y2="32"/></g>
        <path d="M48 30 l-14 18 l-4 2 l1 -4 l14 -18 z" fill="#2a2d86" stroke="#ffffff" stroke-width="2"/>
        <path d="M12 52 l30 0" stroke="#ffffff" stroke-width="2"/>
      </svg>
      <div class="feature__label">Previous Year’s<br>Reference Questions</div>
    </div>
    <div class="feature" style="left:726px">
      <svg width="62" height="62" viewBox="0 0 62 62">
        <circle cx="31" cy="31" r="28" fill="#2a2d86" stroke="#ffffff" stroke-width="3"/>
        <rect x="22" y="8" width="24" height="30" fill="#ffffff" stroke="#2a2d86" stroke-width="1.5"/>
        <rect x="19" y="12" width="24" height="30" fill="#ffffff" stroke="#2a2d86" stroke-width="1.5"/>
        <rect x="16" y="16" width="24" height="30" fill="#ffffff" stroke="#2a2d86" stroke-width="1.5"/>
        <g stroke="#2a2d86" stroke-width="1.8"><line x1="20" y1="23" x2="36" y2="23"/><line x1="20" y1="28" x2="36" y2="28"/><line x1="20" y1="33" x2="36" y2="33"/><line x1="20" y1="38" x2="36" y2="38"/></g>
      </svg>
      <div class="feature__label">Covers Complete<br>Syllabus</div>
    </div>
  </section>

  <div class="dot-band" role="img" aria-label="Decorative band of navy dots on a light blue shimmer"></div>
  <div class="gold-rule"></div>

  <div class="brand">VORLIN EDUCATION</div>
</main>
</body>
</html>
```